Contemporary Elegant Business Card Design for an International Trade Company in the Wine Industry

We need a new business card design for an international trade company in the wine and winemaking industry. The overall feel of the card should be contemporary, upscale, luxurious and elegant. It should communicate confidence and professionalism. The colors should complementary to our logo design (burgundy, gold, and black).
Inspiration: rich velvet tapestry
The card should include the following information:
Business: Brovenna Trading/Shipping, LLC.
Name: Marcus T. Hollenbrand
Title: CEO
Email: mark@brovennatrading.example
Phone: 555-294-6172
www.brovennatrading.example
Updates
Project Deadline Extended
Reason: We'd like the designers that we requested some additional designs from to still submit designs. Thank you!
Industry/Entity Type
Business
Contact Information for Business Card
Title: CEO
Phone: 555-294-6172
www.brovennatrading.example
Look and feel

```html
<!DOCTYPE html>
<html lang="en">
<head>
<meta charset="utf-8">
<title>Brovenna Trading/Shipping — Business Card</title>
<link href="https://fonts.googleapis.com/css2?family=Cinzel:wght@600;700&display=swap" rel="stylesheet">
<style>
  :root {
    --backdrop: #ece6de;
    --card-white: #f7f6f4;
    --damask-white: #ecebe8;
    --burgundy: #7a1420;
    --burgundy-deep: #6a0f1a;
    --gold: #e0a93a;
    --ink: #111111;
  }
  * { margin: 0; padding: 0; box-sizing: border-box; }
  html, body {
    width: 1200px;
    height: 800px;
    overflow: hidden;
    background: var(--backdrop);
  }
  .stage {
    width: 1200px;
    height: 800px;
    display: flex;
    align-items: center;
    justify-content: center;
    gap: 60px;
  }
  .card {
    position: relative;
    width: 520px;
    height: 297px;
    overflow: hidden;
    box-shadow: 0 6px 18px rgba(0, 0, 0, 0.18);
  }
  .card-pattern {
    position: absolute;
    inset: 0;
    width: 100%;
    height: 100%;
  }
  .card-front { background: var(--card-white); }
  .card-back { background: var(--burgundy); }

  .brand {
    position: absolute;
    inset: 0;
    display: flex;
    align-items: center;
    justify-content: center;
    gap: 14px;
  }
  .brand-square {
    width: 54px;
    height: 54px;
    background: var(--burgundy);
  }
  .brand-name {
    font-family: "Cinzel", serif;
    font-weight: 700;
    font-size: 34px;
    letter-spacing: 1px;
    color: var(--ink);
  }

  .contact {
    position: absolute;
    inset: 0;
    display: flex;
    flex-direction: column;
    align-items: center;
    justify-content: center;
    font-family: "Cinzel", serif;
    font-weight: 600;
    color: var(--gold);
    text-align: center;
    padding-top: 6px;
  }
  .contact-name {
    font-size: 22px;
    font-weight: 700;
    letter-spacing: 1px;
  }
  .contact-title {
    font-size: 17px;
    font-weight: 700;
    margin-bottom: 10px;
  }
  .contact-line {
    font-size: 15px;
    letter-spacing: 1.5px;
    line-height: 1.4;
  }
</style>
</head>
<body>
  <main class="stage">
    <section class="card card-front">
      <svg class="card-pattern" viewBox="0 0 520 297" role="img" aria-label="Faint embossed white damask scroll pattern covering the card">
        <defs>
          <radialGradient id="damask-white" cx="50%" cy="50%" r="70%">
            <stop offset="0%" stop-color="#f7f6f4"/>
            <stop offset="100%" stop-color="#e8e7e4"/>
          </radialGradient>
        </defs>
        <rect width="520" height="297" fill="url(#damask-white)"/>
      </svg>
      <div class="brand">
        <span class="brand-square"></span>
        <span class="brand-name">Brovenna</span>
      </div>
    </section>

    <section class="card card-back">
      <svg class="card-pattern" viewBox="0 0 520 297" role="img" aria-label="Subtle tone-on-tone burgundy damask scroll pattern covering the card">
        <defs>
          <radialGradient id="damask-red" cx="50%" cy="45%" r="75%">
            <stop offset="0%" stop-color="#81172a"/>
            <stop offset="100%" stop-color="#6a0f1a"/>
          </radialGradient>
        </defs>
        <rect width="520" height="297" fill="url(#damask-red)"/>
      </svg>
      <div class="contact">
        <p class="contact-name">Marcus T. Hollenbrand</p>
        <p class="contact-title">CEO</p>
        <p class="contact-line">555-294-6172</p>
        <p class="contact-line">MARK@BROVENNATRADING.EXAMPLE</p>
        <p class="contact-line">WWW.BROVENNATRADING.EXAMPLE</p>
      </div>
    </section>
  </main>
</body>
</html>
```